To design a brand identity that is simple and creative with 'Valdor' as the brand name, I like modern simple fonts like helvetica neue, I want to print both sides of the card, I am open to dark front and white back, but the design needs to transfer well to letter heads and email signatures, I am looking for sophisticated and elegant, but open minded about clever and off the wall, I do not do 'boring' Valdor Holdings is the mother company for a small group, specialising in Management & consulting, Software development and construction, we have a high level of integrity, we are transparent and accountable for what we do. my images are provided as a guide only, Im not expecting them to be just copied, Im looking for a creator and passionate thinker, who will put life into their work.

Target Market(s)

usually business minded people who are looking for something different in me, such as leadership, confidence and focus with thinking that is per haps a little outside the box..

Industry/Entity Type

Construction

Requirements
Must have
• clean, minmalistic
Nice to have
• custom logo
Should not have
• boring, traditional

```html
<!DOCTYPE html>
<html lang="en">
<head>
<meta charset="utf-8">
<title>Valdor Holdings — Business Card</title>
<link rel="stylesheet" href="https://fonts.googleapis.com/css2?family=Open+Sans:wght@400;600;700&display=swap">
<style>
  :root {
    --backdrop: #2b2b2b;
    --card: #ffffff;
    --ink: #141414;
    --muted: #8a8a8a;
    --accent: #e8622a;
    --tone-red: #d4222f;
    --tone-purple: #6e2a82;
    --tone-blue: #1ba3dc;
    --tone-green: #7cb636;
    --tone-lime: #cfdc1f;
  }
  * { margin: 0; padding: 0; box-sizing: border-box; }
  html, body {
    width: 1200px; height: 1000px; overflow: hidden;
    background: var(--backdrop);
    font-family: "Open Sans", Arial, sans-serif;
  }
  .business-card {
    position: absolute; left: 150px; top: 240px;
    width: 900px; height: 520px;
    background: var(--card);
    overflow: hidden;
  }
  .edge-feature {
    position: absolute; left: 0; top: 0;
    width: 110px; height: 100%;
    background: linear-gradient(180deg,
      var(--tone-red) 0%,
      var(--tone-purple) 35%,
      var(--tone-blue) 58%,
      var(--tone-green) 80%,
      var(--tone-lime) 100%);
    opacity: 0.9;
  }
  .brand {
    position: absolute; right: 40px; top: 44px;
    display: flex; align-items: center; gap: 10px;
  }
  .brand-mark { width: 16px; height: 16px; background: var(--accent); }
  .brand-name { font-size: 44px; font-weight: 400; color: var(--muted); letter-spacing: 1px; line-height: 1; }
  .contact {
    position: absolute; right: 40px; top: 205px; text-align: right;
  }
  .contact-email { font-size: 46px; font-weight: 700; color: var(--accent); line-height: 1.1; }
  .contact-role { font-size: 32px; font-weight: 400; color: var(--muted); line-height: 1.1; }
  .contact-details { margin-top: 42px; font-size: 25px; color: var(--ink); line-height: 1.45; }
  .services {
    position: absolute; right: 40px; bottom: 38px;
    font-size: 17px; font-weight: 600; color: var(--ink);
  }
</style>
</head>
<body>
  <div class="business-card">
    <div class="edge-feature" role="img" aria-label="Multicoloured decorative edge band in red, purple, blue, green and lime"></div>

    <div class="brand">
      <span class="brand-mark"></span>
      <span class="brand-name">valdor</span>
    </div>

    <div class="contact">
      <p class="contact-email">lena@valdor.holdings</p>
      <p class="contact-role">client ambassador</p>
      <p class="contact-details">m: +61 0400 555 102<br>PO BOX 418 Lakeview 6100</p>
    </div>

    <p class="services">management . software . construction</p>
  </div>
</body>
</html>
```